Banner Ad Design Project

I just launched an affiliate program for my company (Brisk Academy), and I need some web ads and banners created. 6 in total.Here are the specs for the ads:
W120XH90- Small Web Ad
W120XH160- Big Web Ad
W468XH60- Full Banner Ad
W250XH250- Big Banner Ad
W125XH125- Samll Square Ad
W160XH600- Wide Skyscraper
I've uploaded one example I made hower I am looking for a more professional look. You'll also see a few flyers I've uploaded. These will get you an idea of the product.
Here is what I am looking to achieve and a little background on my product:
BRISK Academy’s first course, ‘Ready on Shift’ is a 30 minute interactive training and certification course specifically designed for teens and young adults to better prepare them for the workplace. The training is based on employer feedback, delivered on a peer-to-peer level, industry nonspecific, mobile ready and covers the following challenges:
• Work Ethic
• Social Media
• Cell Phone Issues
• Communication and Manners Matter
• Hygiene and more.
These ads are to catch the eyes of bosses, supervisors and managers. Basically anyone who is looking to improve workplace performance. Our website is www.briskacademy.example. Please look it over for our branding. Thanks so much!
ps- Please make 1/2 static banners and 1/2 animated (gif of flash) banner.
Target Market(s)
Bosses, supervisors and managers. Anyone who employees teenagers and young adults and is looking to train them to better serve their customers.
Industry/Entity Type
Training
Look and feel

```html
<!DOCTYPE html>
<html lang="en">
<head>
<meta charset="utf-8">
<title>Brisk Academy – Banner Set</title>
<link rel="stylesheet" href="https://fonts.googleapis.com/css2?family=Francois+One&family=Roboto+Condensed:wght@400;700&display=swap">
<style>
  :root {
    --bg-dark: #7a7a7a;
    --bg-light: #d2d2d2;
    --blue-deep: #0c3477;
    --blue: #1a52a8;
    --blue-bright: #2a6cc4;
    --yellow: #ffe82a;
    --yellow-deep: #f4b800;
    --white: #ffffff;
    --red: #c8141c;
    --ink: #1a1a1a;
    --brand: #1c3f93;
    --photo-a: #c9a58a;
    --photo-b: #6f7d8e;
  }
  * { box-sizing: border-box; margin: 0; padding: 0; }
  html, body { width: 1200px; height: 1046px; overflow: hidden; }
  body {
    background: linear-gradient(150deg, #8c8c8c 0%, #6e6e6e 35%, #a8a8a8 70%, var(--bg-light) 100%);
    font-family: "Roboto Condensed", "Arial Narrow", sans-serif;
  }
  .stage {
    position: absolute; left: 0; top: 0;
    width: 764px; height: 666px;
    transform: scale(1.5707);
    transform-origin: 0 0;
  }
  .banner {
    position: absolute; overflow: hidden;
    background: linear-gradient(180deg, var(--blue-bright) 0%, var(--blue) 45%, var(--blue-deep) 100%);
    box-shadow: 0 1px 3px rgba(0,0,0,.25);
  }
  .banner > * { position: absolute; }
  .headline {
    font-family: "Francois One", "Arial Narrow", sans-serif;
    color: var(--yellow); text-transform: uppercase; line-height: 1;
    text-shadow: 0 1px 2px rgba(0,0,0,.45);
    white-space: nowrap;
  }
  .body-copy {
    font-family: "Francois One", "Arial Narrow", sans-serif;
    color: var(--white); text-transform: uppercase; text-align: center;
  }
  .bullets { list-style: none; color: var(--white); font-weight: 700; white-space: nowrap; }
  .bullets li::before { content: "✓ "; }
  .cta {
    display: flex; align-items: center; justify-content: center;
    background: linear-gradient(180deg, #fff46a 0%, var(--yellow) 40%, var(--yellow-deep) 100%);
    color: var(--ink); font-weight: 700; border-radius: 4px;
    box-shadow: 0 1px 2px rgba(0,0,0,.5); white-space: nowrap;
  }
  .photo { background: linear-gradient(160deg, var(--photo-a) 0%, #9a8f86 50%, var(--photo-b) 100%); }
  .brand {
    font-family: "Francois One", "Arial Narrow", sans-serif;
    color: var(--brand); text-align: center; line-height: 1; white-space: nowrap;
  }
  .panel { display: block; }

  /* Wide skyscraper 160x600 */
  .sky { left: 49px; top: 39px; width: 160px; height: 600px; }
  .sky .headline.l1 { left: 0; width: 160px; top: 14px; font-size: 34px; text-align: center; }
  .sky .headline.l2 { left: 0; width: 160px; top: 52px; font-size: 27px; text-align: center; }
  .sky .body-copy { left: 4px; width: 152px; top: 93px; font-size: 15.5px; line-height: 21.5px; }
  .sky .cta { left: 13px; top: 258px; width: 134px; height: 31px; font-size: 16px; }
  .sky .photo { left: 0; top: 300px; width: 160px; height: 180px; }
  .sky .panel { left: 0; top: 460px; width: 160px; height: 140px; }
  .sky .brand { left: 0; width: 160px; top: 525px; font-size: 26px; }

  /* Big banner 250x250 */
  .square-lg { left: 251px; top: 39px; width: 250px; height: 250px; }
  .square-lg .panel { left: 130px; top: 0; width: 120px; height: 250px; }
  .square-lg .headline.l1 { left: 6px; top: 20px; font-size: 27px; }
  .square-lg .headline.l2 { left: 6px; top: 52px; font-size: 23px; }
  .square-lg .headline.l3 { left: 6px; top: 80px; font-size: 42px; }
  .square-lg .bullets { left: 6px; top: 142px; font-size: 12px; line-height: 19px; }
  .square-lg .cta { left: 12px; top: 207px; width: 120px; height: 28px; font-size: 15px; }
  .square-lg .photo { left: 134px; top: 92px; width: 116px; height: 158px; }
  .square-lg .brand { left: 152px; width: 96px; top: 30px; font-size: 18px; }

  /* Small square 125x125 */
  .square-sm { left: 532px; top: 82px; width: 125px; height: 125px; }
  .square-sm .panel { left: 65px; top: 0; width: 60px; height: 125px; }
  .square-sm .headline.l1 { left: 3px; top: 10px; font-size: 14px; }
  .square-sm .headline.l2 { left: 3px; top: 27px; font-size: 11.5px; }
  .square-sm .headline.l3 { left: 3px; top: 40px; font-size: 20px; }
  .square-sm .bullets { left: 3px; top: 71px; font-size: 6.2px; line-height: 9.5px; }
  .square-sm .cta { left: 6px; top: 103px; width: 60px; height: 14px; font-size: 7.5px; border-radius: 2px; }
  .square-sm .photo { left: 67px; top: 46px; width: 58px; height: 79px; }
  .square-sm .brand { left: 76px; width: 48px; top: 12px; font-size: 9px; }

  /* Big web ad 120x160 */
  .tall-sm { left: 251px; top: 320px; width: 120px; height: 160px; }
  .tall-sm .headline.l1 { left: 0; width: 120px; top: 4px; font-size: 26px; text-align: center; }
  .tall-sm .headline.l2 { left: 0; width: 120px; top: 31px; font-size: 12.5px; text-align: center; }
  .tall-sm .bullets { left: 6px; top: 49px; font-size: 10px; line-height: 16.5px; }
  .tall-sm .panel { left: 0; top: 100px; width: 120px; height: 60px; }
  .tall-sm .photo { left: 46px; top: 104px; width: 74px; height: 42px; }
  .tall-sm .brand { left: 3px; width: 48px; top: 130px; font-size: 8px; }
  .tall-sm .cta { left: 56px; top: 139px; width: 58px; height: 14px; font-size: 8px; border-radius: 2px; }

  /* Small web ad 120x90 */
  .wide-sm { left: 412px; top: 355px; width: 120px; height: 90px; }
  .wide-sm .headline.l1 { left: 0; width: 120px; top: 4px; font-size: 21px; text-align: center; }
  .wide-sm .headline.l2 { left: 0; width: 120px; top: 29px; font-size: 12.5px; text-align: center; }
  .wide-sm .photo { left: 62px; top: 52px; width: 58px; height: 38px; }
  .wide-sm .cta { left: 8px; top: 65px; width: 56px; height: 14px; font-size: 8px; border-radius: 2px; }
</style>
</head>
<body>
<div class="stage">

  <section class="banner sky" aria-label="Wide skyscraper ad">
    <div class="headline l1">Teaching</div>
    <div class="headline l2">Workplace</div>
    <p class="body-copy">Skills to teens &amp; young adults, transforming them into valued employees &amp; customer service ambassadors.</p>
    <div class="cta">Free Preview!</div>
    <div class="photo" role="img" aria-label="Photo of smiling young students holding books"></div>
    <svg class="panel" viewBox="0 0 160 140" preserveAspectRatio="none" aria-hidden="true">
      <path d="M0 48 Q80 0 160 44 L160 140 L0 140 Z" fill="var(--red)"/>
      <path d="M0 56 Q80 10 160 52 L160 140 L0 140 Z" fill="var(--white)"/>
    </svg>
    <div class="brand">BRISK<br>Academy</div>
  </section>

  <section class="banner square-lg" aria-label="Big banner ad">
    <svg class="panel" viewBox="0 0 120 250" preserveAspectRatio="none" aria-hidden="true">
      <path d="M22 0 Q-6 125 12 250 L120 250 L120 0 Z" fill="var(--red)"/>
      <path d="M30 0 Q2 125 20 250 L120 250 L120 0 Z" fill="var(--white)"/>
    </svg>
    <div class="headline l1">Teaching</div>
    <div class="headline l2">Workplace</div>
    <div class="headline l3">Skills</div>
    <ul class="bullets">
      <li>Covering Social Media.</li>
      <li>Texting &amp; Cell Phones.</li>
      <li>Grooming &amp; Hygiene.</li>
    </ul>
    <div class="cta">Free Preview!</div>
    <div class="photo" role="img" aria-label="Photo of smiling young students holding books"></div>
    <div class="brand">BRISK<br>Academy</div>
  </section>

  <section class="banner square-sm" aria-label="Small square ad">
    <svg class="panel" viewBox="0 0 60 125" preserveAspectRatio="none" aria-hidden="true">
      <path d="M11 0 Q-3 62 6 125 L60 125 L60 0 Z" fill="var(--red)"/>
      <path d="M15 0 Q1 62 10 125 L60 125 L60 0 Z" fill="var(--white)"/>
    </svg>
    <div class="headline l1">Teaching</div>
    <div class="headline l2">Workplace</div>
    <div class="headline l3">Skills</div>
    <ul class="bullets">
      <li>Covering Social Media.</li>
      <li>Texting &amp; Cell Phones.</li>
      <li>Grooming &amp; Hygiene.</li>
    </ul>
    <div class="cta">Free Preview!</div>
    <div class="photo" role="img" aria-label="Photo of smiling young students holding books"></div>
    <div class="brand">BRISK<br>Academy</div>
  </section>

  <section class="banner tall-sm" aria-label="Big web ad">
    <div class="headline l1">Teaching</div>
    <div class="headline l2">Workplace Skills</div>
    <ul class="bullets">
      <li>Covering Social Media.</li>
      <li>Texting &amp; Cell Phones.</li>
      <li>Grooming &amp; Hygiene.</li>
    </ul>
    <div class="photo" role="img" aria-label="Photo of smiling young students holding books"></div>
    <svg class="panel" viewBox="0 0 120 60" preserveAspectRatio="none" aria-hidden="true">
      <path d="M0 18 Q40 4 80 30 L80 60 L0 60 Z" fill="var(--red)"/>
      <path d="M0 23 Q38 10 74 34 L120 36 L120 60 L0 60 Z" fill="var(--white)"/>
    </svg>
    <div class="brand">BRISK<br>Academy</div>
    <div class="cta">Free Preview!</div>
  </section>

  <section class="banner wide-sm" aria-label="Small web ad">
    <div class="headline l1">Teaching</div>
    <div class="headline l2">Workplace Skills</div>
    <div class="photo" role="img" aria-label="Photo of smiling young students holding books"></div>
    <div class="cta">Free Preview!</div>
  </section>

</div>
</body>
</html>
```